New hardcover book cover

I want a striking, eye-catching cover with title, subtitle and a picture.See for previous book covers: www.brightmaplepress.com

Target Market(s)

young, successful entrepreneurs that have built a business in a niche market that they discovered.

Font styles to use
Serif

Colors

Designer to choose colors to be used in the design.

Requirements
Must have
• A book cover that impresses and captures the imagination of those who look at it.
• MY MISTAKE, SORRY.
• Title: Founders Behind the Quiet Trade Boom
• Subtitle: 19 tales of triumph across
• uncovering unseen openings
• Author: Dennis Harwood
• Please use the photo attached, thanks.

```html
<!DOCTYPE html>
<html lang="en">
<head>
<meta charset="utf-8">
<title>Founders Behind the Quiet Trade Boom — Dennis Harwood</title>
<link href="https://fonts.googleapis.com/css2?family=Oswald:wght@500;600&family=Archivo:wght@400;500&display=swap" rel="stylesheet">
<style>
  :root {
    --backdrop: #e1dfd8;
    --navy: #0f2d5e;
    --red: #d6112f;
    --title-red: #e3112e;
    --white: #f1f1ef;
    --band: #f4f4f2;
    --ink: #2b2b2b;
    --photo-deep: #4a4560;
    --photo-mid: #8c9bb1;
    --photo-sky: #b4cfe2;
    --photo-light: #eeecd2;
  }
  * { margin: 0; padding: 0; box-sizing: border-box; }
  html, body {
    width: 1200px; height: 1200px; overflow: hidden;
    background: var(--backdrop);
  }
  .cover {
    position: absolute; left: 220px; top: 50px;
    width: 760px; height: 1100px;
    background: var(--navy);
    display: flex; flex-direction: column;
  }
  .cover-photo {
    height: 592px;
    background: linear-gradient(105deg, var(--photo-deep) 0%, var(--photo-mid) 45%, var(--photo-sky) 72%, var(--photo-light) 100%);
  }
  .author-band {
    height: 46px; background: var(--band);
    display: flex; align-items: center; justify-content: center;
    font-family: "Archivo", sans-serif; font-weight: 500;
    font-size: 25px; letter-spacing: 0.22em; color: var(--ink);
    text-transform: uppercase;
  }
  .title-block {
    position: relative; flex: 1;
  }
  .title {
    position: absolute; left: 60px; top: 22px;
    font-family: "Oswald", sans-serif; font-weight: 600;
    text-transform: uppercase; line-height: 92px;
    font-size: 104px; letter-spacing: -0.01em;
  }
  .title-line { display: flex; align-items: center; white-space: nowrap; height: 92px; }
  .title-lead { color: var(--title-red); }
  .title-main { color: var(--white); }
  .title-joiner {
    display: flex; flex-direction: column;
    color: var(--title-red); font-size: 34px; line-height: 30px;
    margin-right: 8px; text-align: center; font-weight: 500;
  }
  .subtitle-bar {
    position: absolute; left: 0; right: 0; top: 334px; height: 60px;
    background: var(--red);
    display: flex; flex-direction: column; justify-content: center; align-items: center;
    font-family: "Archivo", sans-serif; font-weight: 400;
    font-size: 20px; line-height: 24px; letter-spacing: 0.04em;
    color: var(--white); text-transform: uppercase;
  }
</style>
</head>
<body>
  <main class="cover">
    <div class="cover-photo" role="img" aria-label="Cover photograph: an arrow striking the centre of a target against a bright sky"></div>
    <div class="author-band">Dennis Harwood</div>
    <section class="title-block">
      <h1 class="title">
        <span class="title-line title-lead">Founders</span>
        <span class="title-line">
          <span class="title-joiner"><span>Behind</span><span>the</span></span>
          <span class="title-main">Quiet Trade</span>
        </span>
        <span class="title-line title-main">Boom</span>
      </h1>
      <p class="subtitle-bar">
        <span>19 tales of triumph across</span>
        <span>uncovering unseen openings</span>
      </p>
    </section>
  </main>
</body>
</html>
```